Infographic for Commercial Painting and Flooring Company

We need an Infographic that shows a compelling argument for signing on with Verimbos for a maintenance contract vs a project. The infographic should be easily understood visually so sell the story we have provided. 1) What does the quick view give me? 2) Am I interested in this? 3) Does this bring me any value? 4) Is this “everything I have seen before or something new and different”? Included here is a word document called Maintenance vs Project Notes with the written content and instructions, a logo, and two other marketing pieces they currently use so you can see how their brand is being used. Colors should be on brand. I'd like to get this done ASAP if possible. We do not want this piece to look busy.

I added two images called Sample 1 and Sample 2 to portray the types of infographics we like. Simple and clear. Love the watch with the pie chart built in....a smaller version of that would be great for us based on the notes document I provided.

Target Market(s)

Facilities Manufacturers and owners of manufacturing facilities

Font styles to use
Sans Serif

Colors

Designer to choose colors to be used in the design.

Requirements
Must have
• Simple, clean, tell a clear story
Nice to have
• Iconography, pie chart, Men in hard hat
Should not have
• Too many colors. Stick with the brand colors and maybe a few others. Don't want it too look to busy.

```html
<!DOCTYPE html>
<html lang="en">
<head>
<meta charset="utf-8">
<title>Verimbos – Maintenance vs Project Infographic</title>
<link href="https://fonts.googleapis.com/css2?family=Roboto:ital,wght@0,300;0,400;0,700;0,900;1,400&display=swap" rel="stylesheet">
<style>
  :root{
    --navy:#0d3b6e;
    --olive:#8c8c17;
    --olive-soft:#c9c8a2;
    --cream:#f1f0e4;
    --white:#ffffff;
    --backdrop:#f3f3f3;
  }
  *{box-sizing:border-box;margin:0;padding:0}
  html,body{width:1200px;height:1200px;overflow:hidden;background:var(--backdrop);font-family:'Roboto',Arial,sans-serif;color:var(--navy)}
  .sheet-frame{position:absolute;left:170px;top:0;width:860px;height:1200px;overflow:hidden;box-shadow:0 0 30px rgba(0,0,0,.08)}
  .sheet{position:absolute;left:0;top:0;width:1200px;height:1675px;background:var(--white);transform:scale(0.71642);transform-origin:0 0}
  .abs{position:absolute}
  .hero-wave{left:0;top:0}
  .brand{left:40px;top:40px;display:flex;align-items:center;gap:12px}
  .brand-mark{width:26px;height:26px;background:var(--olive)}
  .brand-name{font-weight:700;font-size:40px;color:var(--navy);letter-spacing:-.5px}
  .headline{left:140px;top:150px;font-size:46px;font-weight:700;line-height:48px;color:var(--navy)}
  .lede{left:140px;top:312px;width:500px;font-size:21px;font-weight:300;line-height:26px}
  .hero-figure{left:830px;top:8px;width:290px;height:460px;border-radius:20px;background:linear-gradient(180deg,rgba(13,59,110,.10),rgba(140,140,23,.18))}
  .rule{height:4px;background:var(--olive)}
  .section-title{left:0;width:1200px;top:513px;text-align:center;font-size:30px;font-weight:700;line-height:34px}
  .pie{width:170px;height:170px}
  .pie text{font-family:'Roboto',Arial,sans-serif;font-weight:700;fill:var(--white);font-size:15px;text-anchor:middle}
  .pie-caption{width:200px;text-align:center;font-size:15.5px;font-weight:300;line-height:19px;border-top:2px solid var(--navy);padding-top:8px}
  .stat-big{font-size:38px;font-weight:700}
  .stat-unit{font-size:20px;font-weight:700}
  .stat-line{font-size:16px;font-weight:300}
  .stat-line b{font-weight:700}
  .partner-title{left:626px;top:1120px;font-size:31px;font-weight:700;line-height:38px}
  .partner-box{left:626px;top:1203px;width:526px;height:302px;background:var(--olive)}
  .pillars{left:650px;top:1272px;color:var(--white)}
  .pillars li{list-style:none;font-size:20px;font-weight:700;line-height:37px}
  .pillars .aligned{border-top:2px solid var(--white);margin-top:6px;padding-top:8px;font-style:italic;font-weight:400;font-size:18px;line-height:18px;width:126px}
  .benefits{left:794px;top:1209px;width:346px;list-style:none}
  .benefits li{height:28px;font-size:13.5px;font-weight:300;line-height:14px;padding:7px 10px 0;color:var(--white)}
  .benefits li.boxed{background:var(--white);color:var(--olive);height:25px;margin-bottom:3px}
  .benefits li.tall{height:28px;padding-top:1px;line-height:14px}
  .focus-fan{left:0;top:1380px}
  .focus-label{color:var(--white);font-size:15px;font-weight:300;line-height:18px;text-align:center;width:160px}
</style>
</head>
<body>
<div class="sheet-frame">
  <div class="sheet">

    <svg class="abs hero-wave" width="1200" height="480" viewBox="0 0 1200 480" aria-hidden="true">
      <defs>
        <linearGradient id="heroFade" x1="0" y1="0" x2="1" y2="0.4">
          <stop offset="0" stop-color="#ffffff"/>
          <stop offset="0.45" stop-color="#e9e8d6"/>
          <stop offset="1" stop-color="#bdbc91"/>
        </linearGradient>
      </defs>
      <path d="M0 0 H1035 C1030 120 940 170 820 220 C700 270 650 420 380 430 C230 436 90 390 0 470 Z" fill="url(#heroFade)"/>
    </svg>

    <div class="abs brand"><span class="brand-mark"></span><span class="brand-name">Verimbos</span></div>

    <h1 class="abs headline">Imagine What You Could Do<br>with An Extra 30%<br>More Time Each Year?</h1>
    <p class="abs lede">Time that you wouldn't need to spend on-boarding a new company every time you have a project or facility upgrade.</p>

    <div class="abs hero-figure" role="img" aria-label="Illustration of a thinking worker in a hard hat with a question-mark thought bubble, standing beside large gears"></div>

    <div class="abs rule" style="left:48px;top:478px;width:1104px"></div>

    <h2 class="abs section-title">It Takes 30+ Hours to Source<br>and Onboard the Most QualifiedVendor...YIKES!</h2>

    <!-- Row 1 -->
    <svg class="abs pie" style="left:158px;top:612px" viewBox="0 0 170 170"><circle cx="85" cy="85" r="83" fill="#8c8c17"/><path d="M85 85 V2 A83 83 0 0 1 156.9 126.5 Z" fill="#0d3b6e"/><text x="127" y="60">4</text><text x="127" y="77">HOURS</text></svg>
    <svg class="abs pie" style="left:396px;top:612px" viewBox="0 0 170 170"><circle cx="85" cy="85" r="83" fill="#8c8c17"/><path d="M85 85 V2 A83 83 0 1 1 49.9 160.2 Z" fill="#0d3b6e"/><text x="122" y="102">7</text><text x="122" y="119">HOURS</text></svg>
    <svg class="abs pie" style="left:635px;top:612px" viewBox="0 0 170 170"><circle cx="85" cy="85" r="83" fill="#8c8c17"/><path d="M85 85 V2 A83 83 0 0 1 168 85 Z" fill="#0d3b6e"/><text x="122" y="48">3</text><text x="122" y="65">HOURS</text></svg>
    <svg class="abs pie" style="left:873px;top:612px" viewBox="0 0 170 170"><circle cx="85" cy="85" r="83" fill="#8c8c17"/><path d="M85 85 V2 A83 83 0 0 1 156.9 126.5 Z" fill="#0d3b6e"/><text x="126" y="56">4</text><text x="126" y="73">HOURS</text></svg>

    <div class="abs pie-caption" style="left:143px;top:797px">Source Vendors &amp; Bidders</div>
    <div class="abs pie-caption" style="left:400px;top:797px">Schedule and Completing a Walkthrough</div>
    <div class="abs pie-caption" style="left:620px;top:797px">Reviewing Estimates</div>
    <div class="abs pie-caption" style="left:858px;top:797px">Phone calls to clarify scope and any big revisions</div>

    <!-- Row 2 -->
    <svg class="abs pie" style="left:158px;top:853px" viewBox="0 0 170 170"><circle cx="85" cy="85" r="83" fill="#8c8c17"/><path d="M85 85 V2 A83 83 0 0 1 156.9 43.5 Z" fill="#0d3b6e"/><text x="117" y="30">2</text><text x="117" y="46">HOURS</text></svg>
    <svg class="abs pie" style="left:396px;top:853px" viewBox="0 0 170 170"><circle cx="85" cy="85" r="83" fill="#8c8c17"/><path d="M85 85 V2 A83 83 0 0 1 156.9 126.5 Z" fill="#0d3b6e"/><text x="127" y="60">4</text><text x="127" y="77">HOURS</text></svg>
    <svg class="abs pie" style="left:635px;top:853px" viewBox="0 0 170 170"><circle cx="85" cy="85" r="83" fill="#8c8c17"/><path d="M85 85 V2 A83 83 0 0 1 168 85 Z" fill="#0d3b6e"/><text x="123" y="48">3</text><text x="123" y="65">HOURS</text></svg>
    <svg class="abs pie" style="left:873px;top:853px" viewBox="0 0 170 170"><circle cx="85" cy="85" r="83" fill="#8c8c17"/><path d="M85 85 V2 A83 83 0 0 1 168 85 Z" fill="#0d3b6e"/><text x="123" y="48">3</text><text x="123" y="65">HOURS</text></svg>

    <div class="abs pie-caption" style="left:143px;top:1038px;width:210px">Present to Decision Maker &amp; Financing Approval</div>
    <div class="abs pie-caption" style="left:381px;top:1038px;width:210px">Negotiations with Vendor</div>
    <div class="abs pie-caption" style="left:620px;top:1038px">Awarding &amp; Purchasing</div>
    <div class="abs pie-caption" style="left:858px;top:1038px">Completing On-Boarding Paperwork</div>

    <!-- Stats -->
    <div class="abs" style="left:152px;top:1108px"><span class="stat-big">20</span><span class="stat-unit">Projects</span> <span class="stat-big" style="font-size:32px">=</span> <span class="stat-big">600</span><span class="stat-unit">Hours</span></div>
    <div class="abs stat-line" style="left:156px;top:1160px">or <b style="font-size:22px">25%</b> of Your Time Per Year....<b>OUGGH!</b></div>
    <div class="abs" style="left:152px;top:1205px"><span class="stat-big" style="font-size:40px">On-Boarding</span> <span class="stat-unit" style="font-size:22px">Once</span> <span class="stat-big" style="font-size:40px">= 1.5 %</span></div>
    <div class="abs stat-line" style="left:152px;top:1263px">of Your Time for the entire year...<b>FOR REAL!</b></div>

    <!-- Partner -->
    <div class="abs rule" style="left:626px;top:1102px;width:526px"></div>
    <h2 class="abs partner-title">You'll Have A Trusted Partner<br>Who Provides...</h2>
    <div class="abs partner-box"></div>
    <ul class="abs pillars">
      <li>Consistency</li>
      <li>Predictability</li>
      <li>Reliability</li>
      <li class="aligned">Aligned with Your Needs</li>
    </ul>
    <ul class="abs benefits">
      <li class="boxed">Safety Is Our #1 Objective</li>
      <li>Adapting to all ofYour Scheduling Requirements</li>
      <li class="boxed">A Single Point of Communication</li>
      <li>Integration w/ your Work Order Process &amp; Project</li>
      <li class="boxed">Tracking</li>
      <li class="tall">A Dedicated Field Team,who Understands<br>the Ins and Outs of Your Facility</li>
      <li class="boxed">Rapid Response Time</li>
      <li>All Tasks and Jobs (Big or Small) Equally Prioritized</li>
      <li class="boxed">Customized Billing and Future Budget Building</li>
      <li>Visual Facility Mapping</li>
    </ul>

    <!-- Focus fan -->
    <svg class="abs focus-fan" width="800" height="295" viewBox="0 1380 800 295" aria-hidden="true">
      <path d="M119 1670 A278 278 0 0 1 675 1670 Z" fill="#0d3b6e"/>
      <line x1="397" y1="1672" x2="257.5" y2="1427.5" stroke="#fff" stroke-width="5"/>
      <line x1="397" y1="1672" x2="536.5" y2="1427.5" stroke="#fff" stroke-width="5"/>
      <!-- phone -->
      <g transform="rotate(-35 327 1600)">
        <rect x="307" y="1568" width="40" height="64" rx="6" fill="#8c8c17"/>
        <rect x="312" y="1575" width="30" height="46" rx="3" fill="#fff"/>
        <circle cx="327" cy="1626" r="2.5" fill="#fff"/>
      </g>
      <!-- cone -->
      <path d="M397 1540 L417 1605 H377 Z" fill="#8c8c17"/>
      <path d="M390.5 1561 H403.5 L407.5 1574 H386.5 Z" fill="#fff"/>
      <path d="M383.5 1584 H410.5 L413.5 1594 H380.5 Z" fill="#fff"/>
      <rect x="370" y="1603" width="54" height="5" fill="#8c8c17"/>
      <!-- gears -->
      <g fill="#8c8c17">
        <circle cx="465" cy="1630" r="14"/>
        <g stroke="#8c8c17" stroke-width="5">
          <line x1="465" y1="1610" x2="465" y2="1650"/><line x1="445" y1="1630" x2="485" y2="1630"/>
          <line x1="451" y1="1616" x2="479" y2="1644"/><line x1="479" y1="1616" x2="451" y2="1644"/>
        </g>
        <circle cx="465" cy="1630" r="5" fill="#fff"/>
        <circle cx="495" cy="1655" r="10"/>
        <g stroke="#8c8c17" stroke-width="4">
          <line x1="495" y1="1640" x2="495" y2="1670"/><line x1="480" y1="1655" x2="510" y2="1655"/>
          <line x1="485" y1="1645" x2="505" y2="1665"/><line x1="505" y1="1645" x2="485" y2="1665"/>
        </g>
        <circle cx="495" cy="1655" r="3.5" fill="#fff"/>
      </g>
    </svg>
    <div class="abs focus-label" style="left:317px;top:1441px">Focus on<br>Safety to ensure<br>it is a priority</div>
    <div class="abs focus-label" style="left:150px;top:1531px">Focus on<br>Communication<br>with Your Team<br>and Customers</div>
    <div class="abs focus-label" style="left:467px;top:1531px;width:180px">Focus on<br>Productivity to ensure<br>you meet all of your<br>business unit's needs</div>

  </div>
</div>
</body>
</html>
```